Website design for commercial and residential security company

we're looking to see some new designs for an established company with no website.

homepage and one inner page

here is a link to the homepage content, sitemap, logo and more.
https://files.brontavel.net/share/7QxmPzLrTw2vNkdJhYcsa9eFgbUoiVwRn?view=open

call to action should be Request A Quote

if you have any questions please send them to us asap

thank you

1 page

Sans Serif

```html
<!DOCTYPE html>
<html lang="en">
<head>
<meta charset="utf-8">
<title>Keystone Guard Solutions — Security Services</title>
<link href="https://fonts.googleapis.com/css2?family=Montserrat:ital,wght@0,400;0,500;0,600;0,700;1,400;1,600;1,700&family=Oswald:wght@400;500&display=swap" rel="stylesheet">
<style>
:root{
  --navy:#0b1526;
  --gold:#d1ab35;
  --gold-dark:#b8952a;
  --white:#ffffff;
  --light:#f2f2f2;
  --grey:#9aa0aa;
  --muted:#8a93a6;
  --text-dark:#1b1b1b;
  --field-border:#7f8793;
}
*{box-sizing:border-box;margin:0;padding:0}
html,body{width:1200px;height:4466px;overflow:hidden}
body{position:relative;font-family:'Montserrat',sans-serif;background:var(--navy);color:var(--white)}
.abs{position:absolute}
section,header,footer{position:absolute;left:0;width:1200px}

/* header */
.site-header{top:0;height:116px;background:var(--navy)}
.brand{position:absolute;display:flex;align-items:center;gap:10px;font-weight:700;color:var(--white);letter-spacing:1px;white-space:nowrap}
.brand .mark{width:14px;height:14px;background:var(--gold)}
.site-header .brand{left:78px;top:40px;font-size:22px}
.nav{position:absolute;top:44px;left:0;font-size:18px;color:#c9ccd2}
.nav a{position:absolute;color:inherit;text-decoration:none;white-space:nowrap}
.nav a.active{color:var(--gold)}
.nav a.active::after{content:"";position:absolute;left:0;right:0;top:32px;height:3px;background:var(--gold)}
.nav-divider{position:absolute;left:957px;top:42px;width:2px;height:30px;background:#c9ccd2}
.search{position:absolute;left:980px;top:50px;width:173px;border-bottom:1px solid #7f8793;font-size:13px;color:var(--gold);padding-bottom:4px}

/* hero */
.hero{top:116px;height:439px;background:linear-gradient(90deg,#f4f4f4 0%,#dcdcdc 45%,#e8e8e8 100%)}
.hero-photo{position:absolute;left:420px;top:0;width:780px;height:439px;background:linear-gradient(100deg,rgba(220,220,220,0) 0%,#cfcfcf 35%,#bdbdbd 70%,#a9a9a9 100%)}
.hero-camera{position:absolute;left:770px;top:20px;width:430px;height:200px;background:radial-gradient(ellipse at 40% 50%,#3a3a3a 0%,#555 45%,rgba(120,120,120,0) 75%)}
.hero-dots{position:absolute;left:44px;top:200px;display:flex;flex-direction:column;gap:6px}
.hero-dots span{width:8px;height:8px;border-radius:50%;background:#b0b0b0}
.hero-dots span:nth-child(2){background:var(--gold)}
.hero-dots span:nth-child(3){background:var(--gold)}
.hero-title{position:absolute;left:148px;top:86px;font-family:'Oswald',sans-serif;font-weight:400;font-size:92px;color:var(--gold);line-height:1}
.hero-sub{position:absolute;left:152px;top:196px;font-size:32px;letter-spacing:24px;color:#555;font-weight:500;white-space:nowrap}
.btn{position:absolute;display:flex;align-items:center;justify-content:center;font-weight:700;color:var(--white);background:var(--gold);font-size:19px}
.btn-grey{background:#8e8e8e}

/* split blocks */
.heading-split{position:absolute;font-size:55px;font-weight:500;line-height:1.05;color:var(--grey)}
.heading-split b{color:var(--gold);font-weight:500}
.lead{position:absolute;font-style:italic;color:var(--gold);font-size:18px;line-height:26px}
.body-copy{position:absolute;color:#c7cbd3;font-size:15px;line-height:27px}
.frame{position:absolute;background:var(--gold)}
.photo{position:absolute}

.mission{top:555px;height:508px;background:var(--navy)}

/* commercial */
.commercial{top:1063px;height:676px;background:var(--gold)}
.commercial-tail{top:1739px;height:434px;background:var(--navy)}
.centered{position:absolute;left:0;width:1200px;text-align:center}
.section-title{font-size:66px;font-weight:500;color:var(--white);letter-spacing:1px}
.commercial-intro{font-size:21.5px;line-height:34px;color:var(--text-dark);font-weight:500;letter-spacing:.5px}
.by-title{font-size:55px;font-weight:500;color:var(--text-dark);letter-spacing:1px}
.card{position:absolute;left:85px;top:1439px;width:839px;height:538px;background:var(--white)}
.card-panel{position:absolute;left:104px;top:1456px;width:517px;height:500px;background:#f7f7f7;padding:40px 18px 0 16px}
.card-panel h3{font-size:21px;font-weight:500;color:var(--gold);line-height:25px;margin:0 0 26px 0;padding-left:0}
.checklist{list-style:none}
.checklist li{display:flex;gap:14px;font-size:15px;line-height:19px;color:#555;margin-bottom:26px}
.checklist svg{flex:none;width:22px;height:22px}
.quote{font-size:25px;line-height:40px;font-style:italic;font-weight:700;color:var(--muted);letter-spacing:1px}

/* band */
.band{top:2173px;height:419px;background:var(--gold)}
.band p{font-size:22px;line-height:37px;color:var(--white);letter-spacing:1px;text-align:center;padding:0 80px}
.band p + p{margin-top:5px}

.residential{top:2592px;height:647px;background:var(--navy)}

/* contact */
.contact{top:3239px;height:888px;background:var(--light)}
.contact-title{font-size:56px;font-weight:500;color:var(--gold);letter-spacing:1px}
.field{position:absolute;border:2px solid var(--field-border);background:var(--light);color:#6f7680;font-size:19px;padding:0 16px;display:flex;align-items:center}
.field.area{align-items:flex-start;padding-top:30px}

/* footer */
.site-footer{top:4127px;height:339px;background:var(--navy)}
.site-footer .brand{left:61px;top:40px;font-size:34px}
.site-footer .brand .mark{width:20px;height:20px}
.footer-about{position:absolute;left:85px;top:122px;width:370px;font-size:14px;line-height:22px;color:var(--gold)}
.footer-head{position:absolute;left:890px;top:34px;font-size:24px;font-weight:700;color:var(--gold)}
.footer-head::after{content:"";position:absolute;left:0;top:44px;width:110px;height:2px;background:var(--gold)}
.footer-rule{position:absolute;left:85px;top:265px;width:1033px;height:1px;background:#4a5366}
</style>
</head>
<body>

<header class="site-header">
  <div class="brand"><span class="mark"></span>KEYSTONE GUARD</div>
  <nav class="nav">
    <a class="active" href="#" style="left:472px">Home</a>
    <a href="#" style="left:561px">About</a>
    <a href="#" style="left:642px">Solutions</a>
    <a href="#" style="left:748px">Resources</a>
    <a href="#" style="left:864px">Contact</a>
  </nav>
  <div class="nav-divider"></div>
  <div class="search">Search</div>
</header>

<section class="hero">
  <div class="hero-photo" role="img" aria-label="Faded grey city office buildings"></div>
  <div class="hero-camera" role="img" aria-label="Dark security camera mounted on a wall arm"></div>
  <div class="hero-dots"><span></span><span></span><span></span></div>
  <h1 class="hero-title">Call to Action</h1>
  <div class="hero-sub">Security Services</div>
  <a class="btn" style="left:156px;top:344px;width:151px;height:51px">Get Quotes</a>
  <a class="btn btn-grey" style="left:333px;top:344px;width:151px;height:51px">Learn more</a>
</section>

<section class="mission">
  <h2 class="heading-split" style="left:85px;top:66px">Our <b>Mission</b></h2>
  <p class="lead" style="left:85px;top:142px;width:460px">To provide our customers with comprehensive security, audio/video, and automation with top notch customer service. We Ensure Security with Smart Tools.</p>
  <p class="body-copy" style="left:85px;top:260px;width:480px">The graded security measures from Keystone Guard Solutions ensure the safety of both residential and commercial property. We provide a wide range of Residential and Commercial Security Solutions.</p>
  <a class="btn" style="left:85px;top:393px;width:151px;height:51px">Read More</a>
  <div class="frame" style="left:652px;top:50px;width:466px;height:331px"></div>
  <div class="photo" role="img" aria-label="Security camera hanging on a pole against a cloudy grey sky" style="left:624px;top:76px;width:468px;height:337px;background:linear-gradient(160deg,#e6e6e6 0%,#a9a9a9 45%,#cfcfcf 100%)"></div>
</section>

<section class="commercial">
  <svg class="abs" style="left:585px;top:30px" width="30" height="44" viewBox="0 0 30 44" aria-hidden="true">
    <circle cx="15" cy="16" r="13" fill="#111"/>
    <path d="M17 6 L10 18 H15 L12 27 L20 14 H15 Z" fill="var(--gold)"/>
    <rect x="9" y="31" width="12" height="4" fill="#111"/>
    <rect x="10" y="37" width="10" height="4" fill="#111"/>
  </svg>
  <h2 class="centered section-title" style="top:88px">Commercial Solutions</h2>
  <p class="centered commercial-intro" style="top:172px;padding:0 95px">People's safety is our top priority. This includes ensuring that the security system built at your commercial property is configured accurately. Further, it will protect against intruders, burglaries, and holdups.</p>
  <h2 class="centered by-title" style="top:300px">We Do This By</h2>
</section>
<section class="commercial-tail">
  <p class="centered quote" style="top:278px;padding:0 100px">We will help secure your company outside of the realm of conventional monitoring technologies. Indeed, we take a customised and comprehensive approach to defence.</p>
</section>

<div class="card"></div>
<div class="card-panel">
  <h3>Protect assets and Security of your business with Exceptional Commercial Security Installation</h3>
  <ul class="checklist">
    <li><svg viewBox="0 0 22 22"><rect x="1" y="3" width="17" height="17" fill="none" stroke="#222" stroke-width="2"/><path d="M5 11 L10 16 L20 3" fill="none" stroke="#222" stroke-width="2.5"/></svg>Audio &amp; Video Solutions for your commercial property</li>
    <li><svg viewBox="0 0 22 22"><rect x="1" y="3" width="17" height="17" fill="none" stroke="#222" stroke-width="2"/><path d="M5 11 L10 16 L20 3" fill="none" stroke="#222" stroke-width="2.5"/></svg>Burglar Alarms &amp; Detectors</li>
    <li><svg viewBox="0 0 22 22"><rect x="1" y="3" width="17" height="17" fill="none" stroke="#222" stroke-width="2"/><path d="M5 11 L10 16 L20 3" fill="none" stroke="#222" stroke-width="2.5"/></svg>CCTV cameras equipped with facial recognition technologies enable the technology to identify the offenders.</li>
    <li><svg viewBox="0 0 22 22"><rect x="1" y="3" width="17" height="17" fill="none" stroke="#222" stroke-width="2"/><path d="M5 11 L10 16 L20 3" fill="none" stroke="#222" stroke-width="2.5"/></svg>Monitoring of alarms and video recordings 24 hours a day, seven days a week. Addressing all the incidents with an urgent response.</li>
    <li><svg viewBox="0 0 22 22"><rect x="1" y="3" width="17" height="17" fill="none" stroke="#222" stroke-width="2"/><path d="M5 11 L10 16 L20 3" fill="none" stroke="#222" stroke-width="2.5"/></svg>Alarm systems and cameras precisely installed so that more of your property is tracked.</li>
  </ul>
</div>
<div class="photo" role="img" aria-label="Close-up of a chrome safe combination dial" style="left:650px;top:1470px;width:550px;height:477px;background:radial-gradient(circle at 40% 48%,#8a8a8a 0%,#2a2a2a 30%,#6e6e6e 45%,#d6d6d6 62%,#c9c9c9 100%)"></div>

<section class="band">
  <div style="padding-top:28px">
    <p>Flooding, smoke, power outages, temperature fluctuations, and other factors will all be tracked. So, you can take prompt steps before you experience damage.</p>
    <p>But, it all comes down to internal and external security measures.</p>
    <p>We can combine low-light cameras, smoke and temperature monitoring, noise control, and physical surveillance into a 24/7 commercial security solution. Thus, you can focus on running your business with utmost safety.</p>
    <p>Our commercial security services are comprehensive. In fact, we have worked out how to protect companies from future threats by tailoring our strategy to each new customer. Therefore, whatever business you are into, we provide you with a security solution that physically protects you, your employees, clients, and property.</p>
  </div>
</section>

<section class="residential">
  <h2 class="heading-split" style="left:85px;top:96px;font-size:52px">Residential<br><b>Security Solutions</b></h2>
  <p class="lead" style="left:85px;top:226px;width:490px">Consider a home surveillance device that would do more for you and your family than you ever imagined.</p>
  <p class="body-copy" style="left:85px;top:318px;width:480px">Keystone Guard Solutions is your trustable security provider. Also, as certified professionals carry out the installation, you have everything under control. Your home is being securely watched from various points, with cameras capable of tracking any intruder's path. Specifically, we offer Residential Intrusion Detection Security Systems, Residential Alarm, Residential Network Wi-Fi, CCTVs and residential home automation.</p>
  <a class="btn" style="left:85px;top:552px;width:151px;height:48px">Read More</a>
  <div class="frame" style="left:664px;top:116px;width:454px;height:413px"></div>
  <div class="photo" role="img" aria-label="Security camera mounted under the eaves of a house" style="left:624px;top:141px;width:472px;height:411px;background:linear-gradient(135deg,#5a4436 0%,#3a2c24 40%,#4b4b4b 60%,#d9d9d9 100%)"></div>
</section>

<section class="contact">
  <h2 class="centered contact-title" style="top:74px">Get in touch with us today!</h2>
  <div class="field" style="left:85px;top:210px;width:482px;height:68px">Full Name</div>
  <div class="field" style="left:636px;top:210px;width:482px;height:68px">Company</div>
  <div class="field" style="left:85px;top:316px;width:482px;height:67px">Email</div>
  <div class="field" style="left:636px;top:316px;width:482px;height:67px">Phone</div>
  <div class="field" style="left:85px;top:422px;width:482px;height:67px">Services Location ( Address )</div>
  <div class="field" style="left:636px;top:422px;width:482px;height:67px">Services Location ( City,State,Zip Code )</div>
  <div class="field area" style="left:85px;top:527px;width:1033px;height:179px">Description of Services (s) Needed, Which Day \ Date ete..</div>
  <a class="btn" style="left:506px;top:770px;width:186px;height:62px;font-size:22px">Submit</a>
</section>

<footer class="site-footer">
  <div class="brand"><span class="mark"></span>KEYSTONE GUARD</div>
  <p class="footer-about">To provide our customers with comprehensive security, audio/video, and automation with top notch customer service. We Ensure Security with Smart Tools.</p>
  <div class="footer-head">Contact Info</div>
  <div class="footer-rule"></div>
</footer>

</body>
</html>
```